Gebrauchtwagenhandel sucht Logo & Visitenkarte
Very good & quick response on all our wishes and ideas. I would like to recommend the designer for his daily constant efforts to work it out - very nice !!
Zielgruppe
Wir betreiben einen Gebrauchtwagenhandel.
Aufgabenstellung
1) Wir möchten das kaufmännische '&' in einer kleineren 2/3 Proportion zu den Buchstaben 'B' & 'G'. Allerdings ohne Freizeichen zusammengeschrieben.
2) Wir möchten ein Logo mit einem vertrauensbildenden Charakter erhalten.
3) Wir möchten nicht eines von diesen Kfz Silhouetten in unserem Logo haben, mit dem jeder zweite Händler antritt.
4) Unsere Rechtsform 'GmbH & Co. KG' soll sich dezent, wie auch immer, auf oder um das Logo bzw. Visitenkarte wiederfinden.
5) Für die Visitenkarten sollen folgende Punkte/Zeilen eingefügt werden ( zwei Geschäftsführer):
- Internetadresse (Nachtrag)
- Email Adresse (Nachtrag)
- Festnetz Nummer (Nachtrag)
- Mobile Nummer (Nachtrag)

```html
<!DOCTYPE html>
<html lang="de">
<head>
<meta charset="utf-8">
<title>K&amp;L Fahrzeughaus – Visitenkarte</title>
<link rel="stylesheet" href="https://fonts.googleapis.com/css2?family=Roboto+Condensed:wght@400;700&display=swap">
<style>
  :root {
    --bg: #eeeeee;
    --card-light: #ffffff;
    --card-dark: #353535;
    --teal: #12a99a;
    --ink: #2b2b2b;
    --ink-soft: #3a3a3a;
    --silver: #d6d6d6;
  }
  * { margin: 0; padding: 0; box-sizing: border-box; }
  html, body {
    width: 1200px; height: 800px; overflow: hidden;
    background: var(--bg);
    font-family: "Roboto Condensed", Arial, sans-serif;
  }
  .sheet {
    position: relative; width: 1200px; height: 800px;
    display: flex; align-items: center; justify-content: center; gap: 60px;
  }
  .card {
    width: 520px; height: 312px; position: relative;
    box-shadow: 0 2px 8px rgba(0,0,0,.12);
  }
  .card--front { background: var(--card-light); color: var(--ink); }
  .card--back { background: var(--card-dark); display: flex; flex-direction: column; align-items: center; justify-content: center; gap: 18px; }

  .brand { display: flex; align-items: center; gap: 12px; }
  .brand__dot { border-radius: 50%; background: var(--teal); flex: none; }
  .brand__name { font-weight: 700; text-transform: uppercase; letter-spacing: .01em; }

  .card--front .brand { position: absolute; left: 128px; top: 58px; }
  .card--front .brand__dot { width: 46px; height: 46px; }
  .card--front .brand__name { font-size: 26px; color: var(--ink-soft); line-height: 1.05; }

  .contact {
    position: absolute; left: 128px; top: 160px;
    display: flex; gap: 16px; font-size: 14px; line-height: 1.35;
  }
  .contact__person .name { color: var(--teal); font-weight: 700; }
  .contact__company { color: var(--ink); }

  .card--back .brand__dot { width: 110px; height: 110px; }
  .card--back .brand__mark { font-size: 52px; color: var(--silver); font-weight: 700; }
  .card--back .brand__name { font-size: 40px; color: var(--silver); letter-spacing: .02em; }
</style>
</head>
<body>
<main class="sheet">
  <section class="card card--front" aria-label="Visitenkarte Vorderseite">
    <div class="brand">
      <span class="brand__dot"></span>
      <span class="brand__name">K&amp;L<br>Fahrzeughaus</span>
    </div>
    <div class="contact">
      <div class="contact__person">
        <div class="name">Jonas Wendrath</div>
        <div class="role">Geschäftsführer</div>
      </div>
      <div class="contact__company">
        <div>K&amp;L Fahrzeughaus GmbH &amp; Co. KG</div>
        <div>Mühlenweg 12</div>
        <div>25482 Lindhorst</div>
        <div>www.kl-fahrzeughaus.de</div>
        <div>info@kl-fahrzeughaus.de</div>
        <div>Tel.: 04120 55 81 37 20</div>
        <div>mobil: 0171 48 26 93 05</div>
      </div>
    </div>
  </section>

  <section class="card card--back" aria-label="Visitenkarte Rückseite">
    <div class="brand">
      <span class="brand__dot"></span>
      <span class="brand__mark">K&amp;L</span>
    </div>
    <div class="brand__name">Fahrzeughaus</div>
  </section>
</main>
</body>
</html>
```